New Brava Tiles Billboard at HQ

Looking to design a catchy image / theme for a billboard located just above our corporate HQ showroom and warehouse, along the service road of a 6-lane highway. Billboard measures 8ft x 24 ft. Would like to highlight that the store location is directly beneath the sign.

We are a retail and wholesale business selling premium flooring, ready to assemble cabinets, and granite countertops. See image ideas attached. Our information:
NAME: Brava Tiles, Cabinets, Countertops
ADDRESS: 412 W. Hwy 29, Cedar Bend, CB 75990
WEBSITE: www.bravatiles-example.com
PHONE: 555-8-DECKED (555-833-2533)

```html
<!DOCTYPE html>
<html lang="en">
<head>
<meta charset="utf-8">
<title>Brava Tiles Billboard</title>
<link rel="stylesheet" href="https://fonts.googleapis.com/css2?family=Montserrat:wght@400;500;600;700;800&display=swap">
<style>
  :root {
    --brand-green: #7dc242;
    --green-edge: #a6d872;
    --ink: #1c1c1c;
    --paper: #ffffff;
    --backdrop: #e6e6e6;
  }
  html, body {
    margin: 0;
    padding: 0;
    width: 919px;
    height: 1200px;
    overflow: hidden;
    background: var(--backdrop);
    font-family: "Montserrat", sans-serif;
  }
  .billboard {
    position: absolute;
    left: 30px;
    top: 457px;
    width: 860px;
    height: 286px;
    box-shadow: 0 10px 28px rgba(0,0,0,0.25);
    background: var(--paper);
  }
  .billboard-art {
    position: absolute;
    inset: 0;
    width: 100%;
    height: 100%;
    display: block;
  }
  .intro {
    position: absolute;
    left: 17px;
    top: 29px;
    width: 320px;
    margin: 0;
    color: var(--paper);
    font-size: 15.5px;
    line-height: 19px;
    font-weight: 500;
  }
  .intro strong { font-weight: 700; }
  .service-label {
    position: absolute;
    top: 156px;
    margin: 0;
    color: var(--paper);
    font-size: 11.5px;
    font-weight: 500;
    letter-spacing: 0.3px;
  }
  .service-floors { left: 16px; }
  .service-cabinets { left: 111px; }
  .service-countertops { left: 188px; }
  .phone {
    position: absolute;
    left: 60px;
    top: 197px;
    margin: 0;
    color: var(--ink);
    font-size: 15px;
    font-weight: 700;
    letter-spacing: 0.5px;
  }
  .phone-digits {
    font-size: 9.5px;
    font-weight: 600;
    margin-left: 4px;
    letter-spacing: 0.3px;
  }
  .website {
    position: absolute;
    left: 60px;
    top: 244px;
    margin: 0;
    color: var(--ink);
    font-size: 11px;
    font-weight: 500;
    letter-spacing: 1px;
  }
  .brand-name {
    position: absolute;
    left: 322px;
    width: 216px;
    top: 52px;
    margin: 0;
    text-align: center;
    color: var(--ink);
    font-size: 34px;
    line-height: 40px;
    font-weight: 800;
    letter-spacing: -0.5px;
  }
  .address {
    position: absolute;
    left: 322px;
    width: 216px;
    top: 185px;
    margin: 0;
    text-align: center;
    color: var(--ink);
    font-size: 10.5px;
    line-height: 17px;
    font-weight: 600;
    font-style: normal;
  }
</style>
</head>
<body>
  <section class="billboard" aria-label="Brava Tiles billboard">
    <svg class="billboard-art" viewBox="0 0 1480 493" preserveAspectRatio="none">
      <defs>
        <linearGradient id="kitchen-tones" x1="0" y1="0" x2="0.4" y2="1">
          <stop offset="0" stop-color="#d9cfc0"/>
          <stop offset="0.3" stop-color="#7a3522"/>
          <stop offset="0.65" stop-color="#5a1d12"/>
          <stop offset="1" stop-color="#a3361a"/>
        </linearGradient>
      </defs>

      <rect x="0" y="0" width="1480" height="493" fill="var(--paper)"/>

      <!-- green information panel -->
      <path d="M0 30 H520 Q555 30 555 65 V240 H760 V493 H0 Z" fill="var(--brand-green)"/>

      <!-- kitchen showroom photo area -->
      <path role="img" aria-label="Photo of a showroom kitchen with cherry wood cabinets, granite island and glossy hardwood floor"
            d="M740 493 V260 H940 V80 Q940 30 990 30 H1480 V493 Z" fill="url(#kitchen-tones)"/>

      <!-- downward pointer marking the store below -->
      <path d="M555 0 H940 V250 Q940 272 955 285 Q963 296 952 306 L760 462 Q740 478 720 462 L528 306 Q517 296 525 285 Q555 272 555 250 Z"
            fill="var(--paper)"/>
      <g fill="none" stroke="var(--green-edge)" stroke-width="7" stroke-linejoin="round">
        <path d="M940 250 Q940 272 955 285 Q963 296 952 306 L760 462 Q740 478 720 462"/>
        <path d="M555 250 Q555 272 525 285 Q517 296 528 306 L720 462"/>
      </g>

      <!-- location line and pin -->
      <line x1="585" y1="277" x2="895" y2="277" stroke="var(--ink)" stroke-width="1.5"/>
      <circle cx="740" cy="277" r="36" fill="var(--paper)" stroke="var(--ink)" stroke-width="1.5"/>
      <circle cx="740" cy="277" r="30" fill="var(--brand-green)"/>
      <path d="M740 296 C732 286 727 279 727 272 A13 13 0 0 1 753 272 C753 279 748 286 740 296 Z" fill="none" stroke="var(--paper)" stroke-width="2.5"/>
      <circle cx="740" cy="272" r="4.5" fill="none" stroke="var(--paper)" stroke-width="2.5"/>

      <!-- service ticks -->
      <g fill="var(--paper)" stroke="var(--green-edge)" stroke-width="3">
        <circle cx="52" cy="236" r="20"/>
        <circle cx="215" cy="236" r="20"/>
        <circle cx="348" cy="236" r="20"/>
      </g>
      <g fill="none" stroke="var(--ink)" stroke-width="4" stroke-linecap="round" stroke-linejoin="round">
        <path d="M44 236 L50 242 L61 230"/>
        <path d="M207 236 L213 242 L224 230"/>
        <path d="M340 236 L346 242 L357 230"/>
      </g>

      <!-- phone badge -->
      <circle cx="62" cy="357" r="27" fill="var(--paper)" stroke="var(--green-edge)" stroke-width="4"/>
      <path d="M53 346 Q50 349 52 355 Q57 366 68 370 Q73 372 76 368 L73 363 L67 364 Q61 360 58 354 L60 349 Z"
            fill="none" stroke="var(--ink)" stroke-width="2" stroke-linejoin="round"/>

      <!-- website pill -->
      <rect x="30" y="404" width="356" height="58" rx="29" fill="var(--paper)"/>
      <circle cx="60" cy="433" r="27" fill="var(--paper)" stroke="var(--brand-green)" stroke-width="4"/>
      <g fill="none" stroke="var(--brand-green)" stroke-width="2">
        <circle cx="60" cy="433" r="14"/>
        <ellipse cx="60" cy="433" rx="6" ry="14"/>
        <line x1="46" y1="433" x2="74" y2="433"/>
        <line x1="48" y1="426" x2="72" y2="426"/>
        <line x1="48" y1="440" x2="72" y2="440"/>
      </g>
    </svg>

    <p class="intro">We are a <strong>retail</strong> and <strong>wholesale</strong><br>business assembling<br><strong>premium flooring, cabinets</strong><br>and <strong>granite countertops.</strong></p>

    <p class="service-label service-floors">Brava Tiles</p>
    <p class="service-label service-cabinets">Cabinets</p>
    <p class="service-label service-countertops">Countertops</p>

    <p class="phone">555-8-DECKED<span class="phone-digits">( 555-833-2533 )</span></p>
    <p class="website">www.bravatiles-example.com</p>

    <h1 class="brand-name">Brava Tiles</h1>
    <address class="address">412 W. Hwy 29, Cedar Bend<br>CB 75990</address>
  </section>
</body>
</html>
```